Company Letter head for real estate company

need company letter head

You can use the logo that I submitted. no need to create a new one

• must have my address on it..38642 MARLOWE, CANTON, MI 48203-1957, INFO@WRKMB.CA

```html
<!DOCTYPE html>
<html lang="en">
<head>
<meta charset="utf-8">
<title>Wrenmark Letterhead</title>
<link href="https://fonts.googleapis.com/css2?family=Arimo:wght@400&family=Tinos:wght@400&display=swap" rel="stylesheet">
<style>
  :root {
    --backdrop: #d9d9da;
    --paper: #f2f2f3;
    --ink: #555557;
    --ink-dark: #2b2b2d;
    --green: #4f8a35;
    --green-light: #7bb83a;
    --black-band: #1c1c1e;
  }
  html, body {
    margin: 0;
    width: 1200px;
    height: 1141px;
    overflow: hidden;
    background: var(--backdrop);
  }
  .letterhead {
    position: absolute;
    left: 332px;
    top: 87px;
    width: 675px;
    height: 948px;
    background: var(--paper);
    box-shadow: 2px 3px 8px rgba(0,0,0,0.25);
    overflow: hidden;
  }
  .brand {
    position: absolute;
    left: 49px;
    top: 62px;
    display: flex;
    align-items: center;
    gap: 8px;
    font-family: "Tinos", serif;
    color: var(--ink-dark);
  }
  .brand-dot {
    width: 14px;
    height: 14px;
    border-radius: 50%;
    background: var(--green);
    flex: none;
  }
  .brand-name {
    font-size: 19px;
    line-height: 1.15;
    letter-spacing: 0.5px;
  }
  .contact {
    position: absolute;
    left: 494px;
    top: 50px;
    font-family: "Tinos", serif;
    font-size: 11px;
    color: var(--ink-dark);
    line-height: 14px;
  }
  .contact-row {
    display: flex;
    align-items: flex-start;
    gap: 7px;
  }
  .contact-row.address { margin-bottom: 5px; }
  .contact-row svg { flex: none; margin-top: 2px; }
  .letter-body {
    position: absolute;
    left: 50px;
    top: 305px;
    width: 575px;
    font-family: "Arimo", sans-serif;
    color: var(--ink);
  }
  .greeting {
    font-size: 17px;
    margin: 0 0 28px;
  }
  .letter-body p {
    font-size: 9.6px;
    line-height: 14.3px;
    text-align: justify;
    margin: 0 0 14.5px;
  }
  .closing {
    margin-top: 34px !important;
  }
  .signature {
    display: block;
    width: 68px;
    height: 26px;
    margin-top: 10px;
    background: linear-gradient(90deg, #3b3e44 0%, #6a6d72 100%);
    opacity: 0.18;
    border-radius: 3px;
  }
  .footer-band {
    position: absolute;
    left: 0;
    bottom: 0;
    width: 675px;
    height: 21px;
  }
</style>
</head>
<body>
  <main class="letterhead">
    <div class="brand">
      <span class="brand-dot"></span>
      <span class="brand-name">WRENMARK<br>Land &amp; Property Development</span>
    </div>

    <div class="contact">
      <div class="contact-row address">
        <svg width="8" height="10" viewBox="0 0 8 10"><path d="M4 0C1.8 0 0 1.7 0 3.8 0 6.5 4 10 4 10s4-3.5 4-6.2C8 1.7 6.2 0 4 0z" fill="var(--green)"/><circle cx="4" cy="3.8" r="1.4" fill="var(--paper)"/></svg>
        <span>38642 Marlowe, Canton<br>Mi 48203-1957</span>
      </div>
      <div class="contact-row">
        <svg width="8" height="9" viewBox="0 0 8 9"><path d="M1.6 0.3 3 2.4 2.2 3.4c.5 1.2 1.3 2 2.4 2.6L5.6 5.2 7.7 6.6 7 8.4C3.4 8.2.2 5 0 1.2z" fill="var(--green)"/></svg>
        <span>(123) 456-7890</span>
      </div>
      <div class="contact-row">
        <svg width="8" height="9" viewBox="0 0 8 9"><rect x="0" y="2" width="8" height="5.5" fill="var(--green)"/><path d="M0 2 4 5 8 2" stroke="var(--paper)" stroke-width="0.8" fill="none"/></svg>
        <span>Info@Wrkmb.Ca</span>
      </div>
      <div class="contact-row">
        <svg width="8" height="9" viewBox="0 0 8 9"><circle cx="4" cy="4.5" r="3.5" fill="none" stroke="var(--green)" stroke-width="0.9"/><path d="M0.5 4.5h7M4 1v7M4 1c-2 2-2 5 0 7M4 1c2 2 2 5 0 7" stroke="var(--green)" stroke-width="0.6" fill="none"/></svg>
        <span>Wrkmb.Ca</span>
      </div>
    </div>

    <section class="letter-body">
      <h1 class="greeting" style="font-weight:400">Dear Mr. Smith,</h1>
      <p>Lorem ipsum dolor sit amet, consectetur adipiscing elit. Donec orci purus, luctus vitae dignissim eu, iaculis sed purus. Vivamus faucibus, ipsum nec aliquet viverra, leo mauris condimentum ligula, sit amet sagittis enim ligula quis arcu. Nam egestas tortor id nisi porttitor mattis. In tortor ante, ultricies in suscipit a, tempus non massa. Vivamus et auctor mi. Fusce vel massa nulla. Phasellus nec eros mauris, et scelerisque orci.</p>
      <p>Donec malesuada orci vitae nulla accumsan porta a id massa. Quisque accumsan iaculis magna sit amet fringilla. Maecenas consequat, magna eget tincidunt semper, odio nibh rutrum mi, id feugiat ante nisi eu risus. Vestibulum nunc orci, rhoncus a placerat in, ultricies in mi. Cras mattis varius eros, vel fringilla nisi suscipit eget. Quisque scelerisque sagittis nulla at porttitor.</p>
      <p>Sed id augue vitae urna euismod commodo aliquet a quam. Pellentesque arcu velit, cursus et malesuada ut, consequat et diam. Nullam erat sem, rhoncus id ullamcorper vitae, rhoncus et arcu. In ultricies ultricies nulla, ut rutrum nisi iaculis at. Donec eu magna a metus ornare faucibus. Fusce aliquet faucibus ultricies. Morbi semper, est id tincidunt gravida, sem arcu adipiscing lacus, ac bibendum nulla leo eu purus. Quisque nec diam sed risus consectetur a ccumsan quis quis nibh. Vestibulum id purus lorem.</p>
      <p>It is a long established fact that a reader will be distracted by the readable content of a page when looking at its layout. The point of using Lorem Ipsum is that it has a more-or-less normal distribution of letters, as opposed to using 'Content here, content here', making it look like readable English. Many desktop publishing packages</p>
      <p>ada ut, consequat et diam. Nullam erat sem, rhoncus id ullamcorper vitae, rhoncus et arcu. In ultricies ultricies nulla, ut rutrum nisi iaculis at. Donec eu magna a metus ornare faucibus. Fusce aliquet faucibus ultricies. Morbi semper,</p>
      <p class="closing">Sincerely,</p>
      <span class="signature" role="img" aria-label="Handwritten signature of the sender"></span>
    </section>

    <svg class="footer-band" viewBox="0 0 675 21" preserveAspectRatio="none" aria-hidden="true">
      <defs>
        <linearGradient id="bandGreen" x1="0" x2="1">
          <stop offset="0" stop-color="var(--green)"/>
          <stop offset="0.5" stop-color="var(--green-light)"/>
          <stop offset="1" stop-color="var(--green)"/>
        </linearGradient>
        <linearGradient id="bandBlack" x1="0" x2="1">
          <stop offset="0" stop-color="var(--black-band)"/>
          <stop offset="0.5" stop-color="#3a3a3c"/>
          <stop offset="1" stop-color="var(--black-band)"/>
        </linearGradient>
      </defs>
      <polygon points="0,0 483,0 470,21 0,21" fill="url(#bandGreen)"/>
      <polygon points="491,0 675,0 675,21 478,21" fill="url(#bandBlack)"/>
    </svg>
  </main>
</body>
</html>
```